Brunelle médico-conseils - word template

We are dooing lot of médical report from word document. We dont print the text on a stationnary. We are producting the report and save it in pdf. So I need à word template. I want something more than just hard the logo. I would like the look of a stationnary in the word template.

I put an exemple of report. But the final don't have to look that way. Propose something more acurate.
After that I will need a business card.

Industry/Entity Type

Medical

Requirements
Must have
• We have to do a design that integrate are logo and color. You have the file in the project.
• The wrihting beteen the title must be in times new roman.
Nice to have
• We have 2 offices:
• Québec (Building Mont-Soleil) 612, ave de Champlain, local 230, G2K 4P7 T.418 527-9143 T.418 527-9186
• St-Romuald (Building Carrefour Beaumont-Les rives) 2450, boul. du Versant-Est, local 310, G7A 3K2. T.418 726-5584 F.418 726-9017
• Mail: info@BrunelleMC.com and expertise@BrunelleMC.com
• Web: www.BrunelleMC.com
• For now you can type www.RDOT.ca to acces the web site.
Should not have
• The same look that the exemple. Because I want to upgrade the look of the company.

```html
<!DOCTYPE html>
<html lang="fr">
<head>
<meta charset="utf-8">
<title>Brunelle médico-conseils – Carte d'affaires</title>
<link rel="stylesheet" href="https://fonts.googleapis.com/css2?family=Roboto:wght@300;400;500;700&display=swap">
<style>
  :root {
    --page-bg: #e9eaec;
    --card-white: #f7f7f8;
    --brand-blue: #1a6fb8;
    --card-blue: #0b5d9c;
    --card-blue-soft: #1466a6;
    --ink: #3a3d42;
    --ink-soft: #6a6e75;
    --rule: #c9ccd1;
    --white: #ffffff;
  }
  * { box-sizing: border-box; margin: 0; padding: 0; }
  html, body {
    width: 1200px;
    height: 900px;
    overflow: hidden;
  }
  body {
    background: var(--page-bg);
    font-family: "Roboto", Arial, sans-serif;
    color: var(--ink);
    position: relative;
  }
  .card {
    position: absolute;
    width: 525px;
    height: 300px;
    box-shadow: 0 10px 24px rgba(0, 0, 0, 0.12);
  }
  .card-front {
    left: 50px;
    top: 300px;
    background: var(--card-white);
  }
  .card-back {
    left: 625px;
    top: 300px;
    background: var(--card-blue);
    overflow: hidden;
  }

  /* Wordmark */
  .wordmark {
    position: absolute;
    display: flex;
    align-items: center;
    gap: 10px;
    font-weight: 500;
    font-size: 25px;
    letter-spacing: 0.2px;
    white-space: nowrap;
  }
  .wordmark-square {
    width: 26px;
    height: 26px;
    flex: none;
  }
  .card-front .wordmark { left: 44px; top: 62px; color: var(--brand-blue); }
  .card-front .wordmark-square { background: var(--brand-blue); }
  .card-back .wordmark { left: 118px; top: 196px; color: var(--white); }
  .card-back .wordmark-square { background: var(--white); }

  /* Person block */
  .person {
    position: absolute;
    left: 96px;
    top: 146px;
  }
  .person-name {
    font-size: 15px;
    font-weight: 500;
    letter-spacing: 0.4px;
    text-transform: uppercase;
    color: var(--ink);
  }
  .person-title {
    margin-top: 3px;
    font-size: 10px;
    color: var(--brand-blue);
  }
  .office-address {
    margin-top: 14px;
    font-size: 11px;
    line-height: 1.45;
    color: var(--ink-soft);
    font-style: normal;
  }

  /* Contact column */
  .contact {
    position: absolute;
    left: 318px;
    top: 142px;
    padding-left: 18px;
    border-left: 1px solid var(--rule);
    list-style: none;
  }
  .contact-item {
    display: flex;
    align-items: center;
    gap: 10px;
    font-size: 11px;
    line-height: 1;
    color: var(--ink-soft);
    margin-bottom: 9px;
  }
  .contact-icon {
    width: 11px;
    height: 11px;
    flex: none;
    fill: none;
    stroke: var(--brand-blue);
    stroke-width: 1.4;
  }

  /* Back decoration */
  .back-tint {
    position: absolute;
    right: -40px;
    top: -60px;
    width: 300px;
    height: 300px;
    background: var(--card-blue-soft);
    transform: rotate(18deg);
    opacity: 0.55;
  }
</style>
</head>
<body>

<section class="card card-front" aria-label="Recto de la carte d'affaires">
  <div class="wordmark">
    <span class="wordmark-square"></span>
    <span class="wordmark-name">Brunelle médico-conseils</span>
  </div>

  <div class="person">
    <p class="person-name">Marc Tremblay</p>
    <p class="person-title">Business Manager</p>
    <address class="office-address">
      Québec (Building Mont-Soleil)<br>
      612, ave de Champlain,<br>
      local 230, G2K 4P7
    </address>
  </div>

  <ul class="contact">
    <li class="contact-item">
      <svg class="contact-icon" viewBox="0 0 12 12" aria-hidden="true">
        <path d="M2.5 1.5 L4.5 1.5 L5.2 4 L4 5 Q5 7.2 7 8 L8 6.8 L10.5 7.5 L10.5 9.5 Q10.5 10.5 9.5 10.5 Q1.5 10 1.5 2.5 Q1.5 1.5 2.5 1.5 Z"/>
      </svg>
      418 527-9100
    </li>
    <li class="contact-item">
      <svg class="contact-icon" viewBox="0 0 12 12" aria-hidden="true">
        <rect x="1" y="2.5" width="10" height="7"/>
        <path d="M1 2.5 L6 6.5 L11 2.5"/>
      </svg>
      info@BrunelleMC.com
    </li>
    <li class="contact-item">
      <svg class="contact-icon" viewBox="0 0 12 12" aria-hidden="true">
        <circle cx="6" cy="6" r="5"/>
        <ellipse cx="6" cy="6" rx="2.2" ry="5"/>
        <path d="M1 6 H11"/>
      </svg>
      www.BrunelleMC.com
    </li>
  </ul>
</section>

<section class="card card-back" aria-label="Verso de la carte d'affaires">
  <div class="back-tint"></div>
  <div class="wordmark">
    <span class="wordmark-square"></span>
    <span class="wordmark-name">Brunelle médico-conseils</span>
  </div>
</section>

</body>
</html>
```